Packaging / Logo Design for Toddler Potty Liners

We need a packaging and logo design for a new company based in Atlanta called "WeeMeadow". We manufacture innovative, eco-friendly baby / toddler products. Our initial product is a flushable, biodegradable potty liner used for toddler potty training. We are looking for a modern / clean / eco-friendly packaging and logo design for this product. Each package will contain 20 liners. Box dimensions are as follows:

Length = 8.5in
Width = 5in
Height = 1.5in

The box will have a perforated top measuring 6.5 inches (see attached pictures). Liners will be folded inside and individually pulled out through the perforated top (similar to a Softrel box). See attached pictures of similar box.

Packaging should appeal to parents as an easy to use, eco-friendly, sanitary solution to potty training. This product is an alternative to the conventional way of cleaning / disinfecting the potty after each use, a process that most parents dread!

The closest competitors are NeatNips (www.neatnips-example.com) and Brillo (www.brillo-example.com) - you can reference their websites to get an idea for the product and use. However, their liners are not flushable and that is the biggest differentiator of this product. Their packaging seems conventional and non-inspiring so we would like our design to stand out from theirs.

We would like to see creative, modern cardboard box designs which will make our brand stand out from the competition. We would like to use one of the following color schemes: 1) a modern green color on a white background, 2) a modern green color on plain cardboard background, or 3) white on a modern green background. May use one or two additional complementary colors. See attached modern green image for inspiration. We would like to see clean lines, text and illustrations. We are looking forward to seeing any cool ideas you may have!
Updates

Brief has been updated with our desired color schemes and pictures for inspiration.  Please read updated brief before beginning your design!  Thanks so much!

Industry/Entity Type

Biodegradable

Requirements
Must have
• The front of the package should include the following info:

Logo: WeeMeadow
Product Name: Flushable Potty Chair Liners
Clean and Convenient
Fits All Potty Chairs
Sewer and Septic Safe
Patent Pending
20 Single-Use Flushable Potty Chair Liners

Package should also have space for some simple instructions (preferably with illustrations). This can be placed on one of the sides of the box.
1. Place liner over clean, dry (underline the word dry) potty bowl.
2. After your toddler uses the potty, remove liner (do not tie) and flush.
3. Give your toddler a high five!

Please submit design considering all sides of the box!

```html
<!DOCTYPE html>
<html lang="en">
<head>
<meta charset="utf-8">
<title>WeeMeadow – Flushable Potty Chair Liners packaging dielines</title>
<link rel="stylesheet" href="https://fonts.googleapis.com/css2?family=Nunito:ital,wght@0,400;0,700;0,800;1,700&display=swap">
<style>
  :root {
    --page-bg: #e6e6e6;
    --card-bg: #ffffff;
    --cut-line: #b9b9b9;
    --accent-pink: #c2307a;
    --count-badge: #7a2a5a;
    --ink: #4a4a4a;
  }
  html, body {
    margin: 0;
    width: 1200px;
    height: 900px;
    overflow: hidden;
  }
  body {
    background: radial-gradient(circle at 60% 45%, #f4f4f4 0%, var(--page-bg) 70%);
    font-family: "Nunito", sans-serif;
    position: relative;
  }
  .sprite { position: absolute; width: 0; height: 0; overflow: hidden; }
  .board-card {
    position: absolute;
    width: 562px;
    height: 420px;
    background: var(--card-bg);
    border-radius: 12px;
    overflow: hidden;
  }
  .board-card--a { left: 20px;  top: 20px; }
  .board-card--b { left: 618px; top: 20px; }
  .board-card--c { left: 20px;  top: 458px; }
  .dieline { width: 100%; height: 100%; display: block; }

  .dieline--white {
    --bg: #ffffff; --tree-fill: url(#trees-white); --band: #a6d13f; --band-dark: #86bb2c; --logo: #6aa321;
  }
  .dieline--mint {
    --bg: #cdeec9; --tree-fill: url(#trees-mint); --band: #6a9a68; --band-dark: #557f55; --logo: #4f7d4f;
  }
  .dieline--lime {
    --bg: #d5f07d; --tree-fill: url(#trees-lime); --band: #3f7d28; --band-dark: #306321; --logo: #3f7d28;
  }

  .panel     { fill: var(--bg); stroke: var(--cut-line); stroke-width: 0.4; }
  .trees     { fill: var(--tree-fill); }
  .band      { fill: var(--band); }
  .band-dark { fill: var(--band-dark); }
  .perforation { fill: none; stroke: #777; stroke-width: 0.4; stroke-dasharray: 1.5 1; }
  .logo-mark { fill: var(--logo); }
  .logo-name { fill: var(--logo); font-weight: 800; font-family: "Nunito", sans-serif; }
  .product-name { fill: var(--accent-pink); font-weight: 700; font-style: italic; font-family: "Nunito", sans-serif; }
  .body-copy { fill: var(--ink); font-size: 2.6px; font-family: "Nunito", sans-serif; }
  .feature  { fill: var(--ink); font-size: 3px; font-family: "Nunito", sans-serif; }
  .feature-dot { fill: var(--accent-pink); }
  .count-badge { fill: var(--count-badge); }
  .count-text { fill: #fff; font-size: 4px; font-weight: 800; font-family: "Nunito", sans-serif; }
  .step-art { fill: #ffffff; stroke: #666; stroke-width: 0.3; }
  .step-num { fill: var(--count-badge); }
  .step-num-text { fill: #fff; font-size: 2.4px; font-weight: 800; font-family: "Nunito", sans-serif; }
  .step-text { fill: #ffffff; font-size: 2.1px; font-family: "Nunito", sans-serif; }
  .step-line { fill: none; stroke: #333; stroke-width: 0.35; stroke-dasharray: 1 0.8; }
</style>
</head>
<body>

<svg class="sprite" aria-hidden="true">
  <symbol id="box-dieline" viewBox="0 0 375 280">
    <!-- lid -->
    <path class="panel" d="M70 25 L95 20 V58 L70 52 Z"/>
    <path class="panel" d="M300 20 L330 25 V52 L300 58 Z"/>
    <rect class="panel" x="95" y="14" width="205" height="78"/>
    <circle class="logo-mark" cx="106" cy="26" r="4"/>
    <text class="logo-name" x="112" y="28" font-size="5">WeeMeadow</text>
    <text class="product-name" x="112" y="36" font-size="3.6">Flushable Potty</text>
    <text class="product-name" x="112" y="40.5" font-size="3.6">Chair Liners</text>
    <text class="body-copy" x="170" y="22">Potty time made simple. Each liner fits over the bowl,</text>
    <text class="body-copy" x="170" y="26">catches every mess and flushes away. Gentle on pipes,</text>
    <text class="body-copy" x="170" y="30">kind to the planet, and easy for tired parents.</text>
    <rect class="trees" x="95" y="48" width="205" height="44" role="img" aria-label="Row of stylised round green trees"/>

    <!-- side band -->
    <path class="band" d="M90 92 L300 88 L365 100 V118 L90 118 Z"/>
    <rect class="band-dark" x="90" y="112" width="275" height="8"/>
    <circle class="count-badge" cx="125" cy="104" r="5"/>
    <text class="count-text" x="125" y="105.5" text-anchor="middle">20</text>

    <!-- back strip -->
    <rect class="panel" x="95" y="120" width="205" height="25"/>
    <text class="body-copy" x="128" y="130">Made from plant based fibres that break down fast. No scrubbing, no soaking, no dread.</text>
    <text class="body-copy" x="128" y="134">Just lift, flush and carry on with your day.</text>

    <!-- front -->
    <path class="panel" d="M90 150 L115 145 V240 L90 235 Z"/>
    <rect class="panel" x="115" y="145" width="170" height="95"/>
    <rect class="panel" x="285" y="145" width="25" height="95"/>
    <path class="panel" d="M310 150 L325 155 V230 L310 235 Z"/>
    <rect class="perforation" x="135" y="150" width="148" height="66" rx="2"/>

    <circle class="logo-mark" cx="148" cy="163" r="4"/>
    <text class="logo-name" x="154" y="165.5" font-size="7">WeeMeadow</text>
    <text class="product-name" x="200" y="178" font-size="6">Flushable Potty</text>
    <text class="product-name" x="212" y="185" font-size="6">Chair Liners</text>

    <circle class="logo-mark" cx="266" cy="160" r="5"/>
    <circle class="feature-dot" cx="278" cy="172" r="0.9"/>
    <text class="feature" x="276" y="173" text-anchor="end">Clean and Convenient</text>
    <circle class="feature-dot" cx="278" cy="177" r="0.9"/>
    <text class="feature" x="276" y="178" text-anchor="end">Fits All Potty Chairs</text>
    <circle class="feature-dot" cx="278" cy="182" r="0.9"/>
    <text class="feature" x="276" y="183" text-anchor="end">Sewer and Septic Safe</text>
    <circle class="feature-dot" cx="278" cy="187" r="0.9"/>
    <text class="feature" x="276" y="188" text-anchor="end">Patent Pending</text>

    <text class="logo-name" x="0" y="0" font-size="5" transform="translate(299 150) rotate(90)">WeeMeadow</text>
    <text class="product-name" x="0" y="0" font-size="3.4" transform="translate(292 150) rotate(90)">Flushable Potty Chair Liners</text>

    <rect class="trees" x="115" y="190" width="170" height="40" role="img" aria-label="Row of stylised round green trees"/>
    <rect class="band" x="115" y="228" width="170" height="12"/>
    <circle class="count-badge" cx="125" cy="236" r="5"/>
    <text class="count-text" x="125" y="237.5" text-anchor="middle">20</text>

    <!-- instruction flap -->
    <path class="band-dark" d="M118 240 H297 L291 276 H124 Z"/>
    <path class="step-line" d="M158 256 Q180 266 196 256 Q218 266 248 256"/>
    <rect class="step-art" x="140" y="244" width="16" height="16" role="img" aria-label="Step 1: liner placed over a dry potty bowl"/>
    <circle class="step-num" cx="142" cy="259" r="2"/>
    <text class="step-num-text" x="142" y="260" text-anchor="middle">1</text>
    <text class="step-text" x="148" y="265" text-anchor="middle">Place liner over</text>
    <text class="step-text" x="148" y="268" text-anchor="middle">clean, dry bowl</text>

    <rect class="step-art" x="196" y="244" width="16" height="16" role="img" aria-label="Step 2: liner lifted out and flushed"/>
    <circle class="step-num" cx="198" cy="259" r="2"/>
    <text class="step-num-text" x="198" y="260" text-anchor="middle">2</text>
    <text class="step-text" x="204" y="265" text-anchor="middle">Remove liner</text>
    <text class="step-text" x="204" y="268" text-anchor="middle">and flush</text>

    <rect class="step-art" x="250" y="244" width="16" height="16" role="img" aria-label="Step 3: high five for the toddler"/>
    <circle class="step-num" cx="252" cy="259" r="2"/>
    <text class="step-num-text" x="252" y="260" text-anchor="middle">3</text>
    <text class="step-text" x="258" y="265" text-anchor="middle">Give a</text>
    <text class="step-text" x="258" y="268" text-anchor="middle">high five!</text>
  </symbol>
</svg>

<div class="board-card board-card--a">
  <svg class="dieline dieline--white" viewBox="0 0 375 280" role="img" aria-label="Dieline, green on white">
    <defs>
      <linearGradient id="trees-white" x1="0" y1="0" x2="0" y2="1">
        <stop offset="0" stop-color="#9ccc3c" stop-opacity="0.1"/>
        <stop offset="0.55" stop-color="#9ccc3c" stop-opacity="0.65"/>
        <stop offset="1" stop-color="#8cc232"/>
      </linearGradient>
    </defs>
    <use href="#box-dieline"/>
  </svg>
</div>
<div class="board-card board-card--b">
  <svg class="dieline dieline--mint" viewBox="0 0 375 280" role="img" aria-label="Dieline, sage green on mint">
    <defs>
      <linearGradient id="trees-mint" x1="0" y1="0" x2="0" y2="1">
        <stop offset="0" stop-color="#5e8f5e" stop-opacity="0.1"/>
        <stop offset="0.55" stop-color="#5e8f5e" stop-opacity="0.65"/>
        <stop offset="1" stop-color="#5a8a5a"/>
      </linearGradient>
    </defs>
    <use href="#box-dieline"/>
  </svg>
</div>
<div class="board-card board-card--c">
  <svg class="dieline dieline--lime" viewBox="0 0 375 280" role="img" aria-label="Dieline, forest green on lime">
    <defs>
      <linearGradient id="trees-lime" x1="0" y1="0" x2="0" y2="1">
        <stop offset="0" stop-color="#4a8a2e" stop-opacity="0.1"/>
        <stop offset="0.55" stop-color="#4a8a2e" stop-opacity="0.7"/>
        <stop offset="1" stop-color="#44842a"/>
      </linearGradient>
    </defs>
    <use href="#box-dieline"/>
  </svg>
</div>

</body>
</html>
```